Home page and features page design for SaaS company

We're looking for designs for a home page and a features page of a new website (possibly more pages to be commissioned thereafter). The website is called 'Brightly Afloat' and is a service that helps swimming clubs and schools reduce administration.

The website will have a clean, minimalist, modern feel but not corporate. Here's an idea of the type of style: https://squadlio.net/pages/payments

At the top of the home page (above the fold) will show the two personas that the website is targeting (Swimming clubs and Swimming Schools) on a styled background (no cheesy stock images please!). Those personas can be represented as an illustration (see page 2 for an example), line art graphic or icon and will link through to a features page.

For your information, the type of people that are members of swimming clubs include beginners, competitive squads and adult swimmers. People that attend a swimming school are typically children learning to swim. If you can represent the above in simple line art illustrations/graphics/icons that match the style of our logo - great!

Below the fold on the home page will be an illustration of the main functions of the site (with our logo central to that) and at the bottom of the page will be what they get for free, testimonials and a call to action for booking a demo.

I've attached a simple wireframe of the home page for your information.

The second page is the features page. This summarises the benefits of each major feature. Each feature listed on the page is separated by a call to action. Here's a link to the content of the features page: http://webhost4.qarvik-advisory.com/KLTsalespages/swimming/swim-club-management-software.html

Don't take a lead from the look / feel / design of this page. I don't like it (hence I'm on here to find a better design!). One thing I'd like to incorporate is a snippet preview of a screenshot on the features page (a bit like in the example). The user can click on this and the full screenshot will load in a pop-up.

The style of the features page should flow from the home page.
Updates

Project Deadline Extended
Reason: Extending deadline to allow more quality designs and give those that have submitted time to make any revisions.

Target Market(s)

Swimming clubs and swimming schools

Industry/Entity Type

Internet

Number of Pages Required

2 page

Font styles to use
Sans Serif

Colors
33a6d7
33b8a4

Requirements
Must have
• Clean, minimalist, modern feel but not corporate. Here's an idea of the type of style: https://squadlio.net/pages/payments
Should not have
• Unstylised stock photographs

```html
<!DOCTYPE html>
<html lang="en">
<head>
<meta charset="utf-8">
<title>Brightly Afloat – Membership software for swimming clubs and schools</title>
<link href="https://fonts.googleapis.com/css2?family=Open+Sans:wght@300;400;600;700&display=swap" rel="stylesheet">
<style>
:root{
  --teal:#33b8a4;
  --teal-deep:#2aa894;
  --blue:#33a6d7;
  --btn-blue:#1f8fe0;
  --navy:#3d4458;
  --salmon:#ee7d76;
  --grey:#97a6a3;
  --ink:#2b2b2b;
  --muted:#6b6b6b;
  --line:#dcdcdc;
  --white:#ffffff;
  --green-a:#2fae79;
  --green-b:#44bc86;
}
*{box-sizing:border-box;margin:0;padding:0}
html,body{width:1200px;height:2479px;overflow:hidden}
body{font-family:"Open Sans",Arial,sans-serif;color:var(--ink);background:var(--white);position:relative}
.abs{position:absolute}

/* hero */
.hero{position:absolute;left:0;top:0;width:1200px;height:702px;
  background:linear-gradient(180deg,#3bbfb0 0%,#33b8a4 55%,#2fb39c 100%);}
.hero-scene{position:absolute;inset:0;background:radial-gradient(ellipse at 30% 40%,rgba(255,255,255,.08),transparent 60%),radial-gradient(ellipse at 80% 30%,rgba(20,110,100,.18),transparent 55%)}
.brand{position:absolute;display:flex;align-items:center;gap:10px;font-weight:700;color:var(--white)}
.brand-dot{width:26px;height:26px;border-radius:50%;background:var(--white)}
.hero .brand{left:91px;top:40px;font-size:25px}
.nav{position:absolute;top:46px;left:456px;display:flex;gap:28px;font-size:15px;color:var(--white)}
.nav-signin{position:absolute;left:1030px;top:40px;width:81px;height:33px;border:2px solid var(--white);border-radius:17px;color:var(--white);font-size:14px;font-weight:600;display:flex;align-items:center;justify-content:center}
.nav-rule{position:absolute;left:91px;top:89px;width:1020px;height:1px;background:rgba(255,255,255,.35)}
.hero-title{position:absolute;top:164px;width:100%;text-align:center;color:var(--white);font-size:43px;font-weight:600}
.hero-sub{position:absolute;top:222px;width:100%;text-align:center;color:var(--white);font-size:23px;font-weight:600}
.persona{position:absolute;top:304px;width:300px;text-align:center}
.persona-art{display:block;margin:0 auto}
.persona-name{margin-top:24px;color:var(--white);font-size:25px;font-weight:600;letter-spacing:.5px}
.persona-btn{display:inline-flex;align-items:center;justify-content:center;gap:6px;margin-top:14px;width:152px;height:35px;border-radius:18px;background:var(--btn-blue);color:var(--white);font-size:15px}

/* features ring */
.functions{position:absolute;left:0;top:702px;width:1200px;height:584px}
.fn-label{font-size:17px;fill:#333;font-family:"Open Sans",Arial,sans-serif}

/* benefits */
.benefits{position:absolute;left:0;top:1286px;width:1200px;height:421px;background:linear-gradient(135deg,#2fa4da,#36abdb 50%,#2c9fd6)}
.benefit{position:absolute;width:470px}
.benefit-icon{position:absolute;left:0;top:0;width:94px;height:94px;border:2px solid rgba(255,255,255,.8);border-radius:50%;display:flex;align-items:center;justify-content:center}
.benefit-title{position:absolute;left:112px;top:4px;color:var(--white);font-size:21px;font-weight:600;white-space:nowrap}
.benefit-text{position:absolute;left:112px;top:38px;width:350px;color:var(--white);font-size:13.5px;line-height:21px}

/* testimonials */
.testimonials-title{position:absolute;top:1770px;width:100%;text-align:center;font-size:28px;font-weight:400;color:#222}
.testimonial{position:absolute;top:1866px;width:520px}
.testimonial-photo{position:absolute;left:0;top:0;width:94px;height:94px;border-radius:50%}
.testimonial-quote{position:absolute;left:128px;top:10px;width:322px;font-size:12.5px;line-height:24px;color:#444;text-align:justify}
.testimonial-quote::before{content:"\201C";position:absolute;left:-18px;top:-8px;font-size:30px;color:var(--blue);font-family:Georgia,serif}
.testimonial-role{position:absolute;left:128px;top:92px;font-size:11px;font-weight:700;color:#222}

/* cta */
.cta{position:absolute;left:0;top:2050px;width:1200px;height:120px;background:linear-gradient(100deg,var(--green-a),var(--green-b) 45%,#3ab47e)}
.cta-title{position:absolute;left:98px;top:20px;font-size:27px;color:var(--white)}
.cta-text{position:absolute;left:98px;top:60px;font-size:17px;color:var(--white)}
.cta-btn{position:absolute;left:904px;top:38px;width:187px;height:47px;border-radius:24px;background:var(--white);color:#333;font-size:21px;display:flex;align-items:center;justify-content:center}

/* footer */
.footer .brand{left:91px;top:2280px;font-size:20px;color:#2f92d4;font-weight:700}
.footer .brand-dot{background:#2f92d4;width:22px;height:22px}
.footer-head{position:absolute;top:2226px;font-size:15px;color:#333}
.footer-text{position:absolute;font-size:12.5px;line-height:22px;color:#666}
.mail-input{position:absolute;left:658px;top:2306px;width:148px;height:32px;border:1px solid #ccc;font-size:12px;color:#777;padding:7px 6px}
.mail-submit{position:absolute;left:806px;top:2306px;width:58px;height:32px;background:var(--teal);color:var(--white);font-size:12.5px;display:flex;align-items:center;justify-content:center}
.social{position:absolute;top:2272px;left:932px;display:flex;gap:14px}
.social span{width:24px;height:24px;border-radius:4px;background:#5a5a5a}
.footer-rule{position:absolute;left:86px;top:2387px;width:1022px;height:1px;background:var(--line)}
.copyright{position:absolute;top:2418px;width:100%;text-align:center;font-size:13px;color:#333}
</style>
</head>
<body>

<section class="hero">
  <div class="hero-scene" role="img" aria-label="Soft illustrated poolside scene with sun loungers, umbrella and trees tinted in teal"></div>
  <div class="brand"><span class="brand-dot"></span>Brightly Afloat</div>
  <nav class="nav"><span>ABOUT US</span><span>PRICING</span><span>FREE RESOURCES</span><span>FREE ACCOUNT</span><span>CONTACT US</span></nav>
  <div class="nav-signin">SIGN-IN</div>
  <div class="nav-rule"></div>
  <h1 class="hero-title">Membership software</h1>
  <p class="hero-sub">For swimming clubs and schools</p>

  <div class="persona" style="left:224px">
    <svg class="persona-art" width="162" height="188" viewBox="0 0 162 188" role="img" aria-label="Illustration of a swimming club coach holding a clipboard">
      <polygon points="81,2 159,47 159,141 81,186 3,141 3,47" fill="#f3f7f7"/>
    </svg>
    <div class="persona-name">SWIMMING CLUBS</div>
    <div class="persona-btn">Find out more <span>»</span></div>
  </div>
  <div class="persona" style="left:662px">
    <svg class="persona-art" width="162" height="188" viewBox="0 0 162 188" role="img" aria-label="Illustration of a child swimming with goggles in blue water">
      <defs><linearGradient id="kid" x1="0" y1="0" x2="0" y2="1"><stop offset="0" stop-color="#f6f3ee"/><stop offset="1" stop-color="#bfe6f7"/></linearGradient></defs>
      <polygon points="81,2 159,47 159,141 81,186 3,141 3,47" fill="url(#kid)"/>
    </svg>
    <div class="persona-name">SWIMMING SCHOOLS</div>
    <div class="persona-btn">Find out more <span>»</span></div>
  </div>
</section>

<section class="functions">
  <svg width="1200" height="584" viewBox="0 0 1200 584">
    <g fill="none" stroke-width="14">
      <circle cx="618" cy="286" r="130" stroke="var(--teal)" stroke-dasharray="81.7 735" transform="rotate(-126 618 286)"/>
      <circle cx="618" cy="286" r="130" stroke="var(--navy)" stroke-dasharray="81.7 735" transform="rotate(-81 618 286)"/>
      <circle cx="618" cy="286" r="130" stroke="var(--salmon)" stroke-dasharray="81.7 735" transform="rotate(-36 618 286)"/>
      <circle cx="618" cy="286" r="130" stroke="var(--grey)" stroke-dasharray="81.7 735" transform="rotate(9 618 286)"/>
      <circle cx="618" cy="286" r="130" stroke="var(--teal)" stroke-dasharray="81.7 735" transform="rotate(54 618 286)"/>
      <circle cx="618" cy="286" r="130" stroke="var(--navy)" stroke-dasharray="81.7 735" transform="rotate(99 618 286)"/>
      <circle cx="618" cy="286" r="130" stroke="var(--salmon)" stroke-dasharray="81.7 735" transform="rotate(144 618 286)"/>
      <circle cx="618" cy="286" r="130" stroke="var(--grey)" stroke-dasharray="81.7 735" transform="rotate(189 618 286)"/>
    </g>
    <circle cx="598" cy="286" r="14" fill="#1f8fe0"/>
    <text x="620" y="293" font-family="Open Sans, Arial, sans-serif" font-weight="700" font-size="19" fill="#1f8fe0">Brightly</text>
    <text x="555" y="318" font-family="Open Sans, Arial, sans-serif" font-weight="700" font-size="19" fill="#1f8fe0">Afloat</text>
    <g fill="none" stroke-width="1.5">
      <polyline points="607,124 607,158" stroke="var(--teal)"/>
      <polyline points="703,199 727,161 818,161" stroke="var(--navy)"/>
      <polyline points="747,281 790,281" stroke="var(--salmon)"/>
      <polyline points="703,369 736,402 843,402" stroke="var(--grey)"/>
      <polyline points="630,422 630,463" stroke="var(--teal)"/>
      <polyline points="421,425 504,425 537,389" stroke="var(--navy)"/>
      <polyline points="438,305 488,305" stroke="var(--salmon)"/>
      <polyline points="397,181 479,181 509,212" stroke="var(--grey)"/>
    </g>
    <text class="fn-label" x="607" y="110" text-anchor="middle">ONLINE PAYMENTS</text>
    <text class="fn-label" x="830" y="167">FINANCIAL REPORTING</text>
    <text class="fn-label" x="799" y="287">MEMBERSHIP DATA</text>
    <text class="fn-label" x="851" y="408">GROUP EMAIL</text>
    <text class="fn-label" x="630" y="484" text-anchor="middle">GALAS</text>
    <text class="fn-label" x="395" y="431" text-anchor="end">EVENT MANAGEMENT</text>
    <text class="fn-label" x="425" y="311" text-anchor="end">ATTENDANCE REGISTER</text>
    <text class="fn-label" x="381" y="187" text-anchor="end">ONLINE REGISTRATIONS</text>
  </svg>
</section>

<section class="benefits" role="img" aria-label="Blue marbled water texture background">
  <div class="benefit" style="left:88px;top:98px">
    <div class="benefit-icon"><svg width="40" height="40" viewBox="0 0 40 40"><path d="M8 33 L22 19 M22 19 a8 8 0 1 0 4-12 l-4 5 3 3 5-4 a8 8 0 0 1-8 7" fill="none" stroke="#fff" stroke-width="4" stroke-linecap="round"/></svg></div>
    <div class="benefit-title">ACCESS TO EXCLUSIVE TOOLS</div>
    <div class="benefit-text">We have over 100 great features and functions to help cut down admin and increase payment collection</div>
  </div>
  <div class="benefit" style="left:649px;top:98px">
    <div class="benefit-icon"><svg width="42" height="34" viewBox="0 0 42 34"><rect x="7" y="4" width="28" height="19" rx="2" fill="none" stroke="#fff" stroke-width="2.5"/><path d="M2 28 H40" stroke="#fff" stroke-width="3" stroke-linecap="round"/></svg></div>
    <div class="benefit-title">ACCOUNT SETUP</div>
    <div class="benefit-text">We take time to understand how your club works and set your account to maximise efficiencies.</div>
  </div>
  <div class="benefit" style="left:88px;top:240px">
    <div class="benefit-icon"><svg width="44" height="40" viewBox="0 0 44 40"><circle cx="16" cy="22" r="9" fill="none" stroke="#fff" stroke-width="5" stroke-dasharray="4 3"/><circle cx="16" cy="22" r="3" fill="#fff"/><circle cx="33" cy="11" r="6" fill="none" stroke="#fff" stroke-width="4" stroke-dasharray="3 2"/><circle cx="33" cy="30" r="5" fill="none" stroke="#fff" stroke-width="3.5" stroke-dasharray="3 2"/></svg></div>
    <div class="benefit-title">SOFTWARE UPDATES</div>
    <div class="benefit-text">We continuously listen to our clients and develop functionality in line with their feedback to help you improve efficiencies and save time</div>
  </div>
  <div class="benefit" style="left:649px;top:240px">
    <div class="benefit-icon"><svg width="36" height="38" viewBox="0 0 36 38"><rect x="3" y="16" width="7" height="18" fill="none" stroke="#fff" stroke-width="2.5"/><path d="M10 17 L17 5 c3 0 4 2 3 6 l-1 4 h10 c3 0 4 3 2 5 c2 2 1 4-1 5 c1 2 0 4-2 4 c1 2-1 4-3 4 H10" fill="none" stroke="#fff" stroke-width="2.5" stroke-linejoin="round"/></svg></div>
    <div class="benefit-title">FIRST CLASS SUPPORT</div>
    <div class="benefit-text" style="width:350px">From your first training session to ongoing support, we're here to help you get the best from the system. You can reach us by chat, email or CallNest 6 days a week.</div>
  </div>
</section>

<h2 class="testimonials-title">TESTIMONIALS</h2>
<div class="testimonial" style="left:98px">
  <div class="testimonial-photo" role="img" aria-label="Portrait photo of a smiling client" style="background:radial-gradient(circle at 50% 45%,#c98d72,#6e3b2a)"></div>
  <p class="testimonial-quote">It is a long established fact that a reader will be distracted by the readable content of a page when looking at its layout. The point of using Lorem Ipsum</p>
  <div class="testimonial-role">CEO, INSURANCE BROKERAGE</div>
</div>
<div class="testimonial" style="left:651px">
  <div class="testimonial-photo" role="img" aria-label="Portrait photo of a smiling client" style="background:radial-gradient(circle at 50% 45%,#d8b39a,#7a5a44)"></div>
  <p class="testimonial-quote">It is a long established fact that a reader will be distracted by the readable content of a page when looking at its layout. The point of using Lorem Ipsum</p>
  <div class="testimonial-role">CEO, INFORMATION TECHNOLOGY CONSULTANCY</div>
</div>

<section class="cta" role="img" aria-label="Green band with soft faceted geometric texture">
  <div class="cta-title">BOOK A FREE DEMO NOW</div>
  <div class="cta-text">Neque porro quisquam est qui dolorem ipsum quia dolor sit amet consectetur, adipisci velit</div>
  <div class="cta-btn">BOOK NOW</div>
</section>

<footer class="footer">
  <div class="brand"><span class="brand-dot"></span>Brightly Afloat</div>
  <div class="footer-head" style="left:364px">CONTACT US</div>
  <div class="footer-text" style="left:364px;top:2262px">Address : 14 Larkmoor Rd, Old Quay<br>Bristol, BS2 9XY<br>Phone : 07700 900 412<br>Email : hello@brightlyafloat.com</div>
  <div class="footer-head" style="left:658px">JOIN OUR MAILING LIST</div>
  <div class="footer-text" style="left:658px;top:2258px;width:215px;font-size:12px;line-height:19px">Your about us information would fit here nicely.</div>
  <div class="mail-input">Email address</div>
  <div class="mail-submit">Submit</div>
  <div class="footer-head" style="left:932px">FOLLOW US OUT THERE</div>
  <div class="social"><span></span><span></span><span></span><span></span></div>
  <div class="footer-rule"></div>
  <div class="copyright">Copyright © 2017. All Rights Reserved</div>
</footer>

</body>
</html>
```